Business Card Design Project

I would like to redesign our business cards and change the look and feel of our marketing material, but maintain the same basic identity of our current logo.
It is my belief that it could be much better.
You can view our website at kducn.com

   

I was looking for a completely different look.  Something much more hip and cool looking.  You can change the colors.

I like this look and feel

 http://www.hudlawfirm.com

 But obviously don’t want to copy them exactly.

 

For the back just leave the last point.

“Focus on Your Business, and We’ll Focus on Your Claim”

I want there to be space for someone to write on.

                                                                    

                                       

I like this look and feel

 http://www.hudlawfirm.com

```html
<!DOCTYPE html>
<html lang="en">
<head>
<meta charset="utf-8">
<title>Northgate Claimworks — Business Cards</title>
<link rel="stylesheet" href="https://fonts.googleapis.com/css2?family=Source+Sans+3:wght@600;700&display=swap">
<style>
  :root{
    --blue-dark:#176482;
    --blue-mid:#1b8db5;
    --blue-light:#23a9d1;
    --ink:#222;
    --card-hi:#ffffff;
    --card-lo:#d6d6d6;
    --page:#ffffff;
  }
  *{margin:0;padding:0;box-sizing:border-box}
  html,body{width:1200px;height:1000px;overflow:hidden;background:var(--page)}
  body{position:relative;font-family:"Source Sans 3",Arial,sans-serif}

  .brand-header{position:absolute;left:178px;top:32px;display:flex;align-items:center;gap:24px}
  .brand-header .brand-mark{width:120px;height:120px;background:var(--blue-mid);margin:10px 0}
  .brand-header .brand-name{font-size:54px;font-weight:700;color:var(--blue-dark);letter-spacing:0.5px;line-height:1}

  .card{position:absolute;width:560px;height:325px;border-radius:30px;overflow:hidden;
    background:radial-gradient(ellipse at 45% 40%,var(--card-hi) 0%,#f1f1f1 35%,var(--card-lo) 100%);
    box-shadow:0 2px 8px rgba(0,0,0,.25);border:3px solid #f4f4f4}
  .card-front-1{left:30px;top:248px}
  .card-front-2{left:33px;top:633px}
  .card-back{left:624px;top:343px;height:322px}
  .card .waves{position:absolute;inset:0;width:100%;height:100%}

  .card-logo{position:absolute;left:20px;top:20px;display:flex;align-items:center;gap:12px}
  .card-logo .brand-mark{width:48px;height:48px;background:var(--blue-mid)}
  .card-logo .brand-name{font-size:21px;font-weight:700;color:var(--blue-dark);line-height:22px}
  .card-tagline{position:absolute;left:22px;top:82px;font-size:15px;font-weight:600;color:var(--blue-mid)}

  .contact{position:absolute;right:38px;text-align:right}
  .contact .person{font-size:29px;font-weight:700;color:var(--blue-dark);line-height:1}
  .contact .role{font-size:13px;font-weight:600;color:var(--blue-light);margin-top:2px}
  .contact .address{font-size:17px;font-weight:600;color:var(--ink);line-height:23px}
  .contact .row{font-size:17px;font-weight:600;color:var(--ink);line-height:23px;margin-top:1px}
  .contact .label{color:var(--blue-mid);margin-right:10px}
  .card-front-1 .contact{top:128px}
  .card-front-1 .contact .address{margin-top:24px}
  .card-front-2 .contact{top:128px}
  .card-front-2 .contact .address{margin-top:22px}

  .site{position:absolute;font-size:16px;font-weight:700;color:#fff;letter-spacing:.3px}
  .card-front-1 .site,.card-front-2 .site{left:30px;bottom:18px}
  .card-back .site{right:24px;bottom:20px}

  .guide-banner{position:absolute;right:0;top:22px;width:310px;height:50px}
  .guide-banner-text{position:absolute;right:16px;top:22px;height:34px;line-height:34px;font-size:20px;font-weight:700;color:#fff;letter-spacing:.4px}
  .promise{position:absolute;left:60px;top:82px;font-size:19px;font-weight:700;color:var(--blue-dark);line-height:21px}
  .promise .accent{color:var(--blue-light)}
  .promise .line-2{padding-left:183px}
</style>
</head>
<body>

<header class="brand-header">
  <span class="brand-mark"></span>
  <span class="brand-name">NORTHGATE CLAIMWORKS</span>
</header>

<section class="card card-front-1">
  <svg class="waves" viewBox="0 0 560 325" preserveAspectRatio="none" aria-hidden="true">
    <path d="M0,128 C60,185 140,232 260,266 C160,252 60,212 0,172 Z" fill="var(--blue-dark)"/>
    <path d="M0,168 C80,222 200,266 420,298 C470,304 520,300 560,292 L560,325 L0,325 Z" fill="var(--blue-mid)"/>
    <path d="M180,264 C300,292 450,300 560,289 L560,304 C450,312 320,300 180,264 Z" fill="var(--blue-light)"/>
  </svg>
  <div class="card-logo">
    <span class="brand-mark"></span>
    <span class="brand-name">Northgate<br>Claimworks</span>
  </div>
  <div class="card-tagline">Gulf Claims Specialists</div>
  <div class="contact">
    <div class="person">Daniel Hartwell</div>
    <div class="address">410 Linden Avenue, Maple Grove, NY 11790</div>
    <div class="row"><span class="label">phone :</span>(555) 014-2287</div>
    <div class="row"><span class="label">cell :</span>(555) 019-3361</div>
    <div class="row"><span class="label">email :</span>dh@kducn.com</div>
  </div>
  <div class="site">www.kducn.com</div>
</section>

<section class="card card-front-2">
  <svg class="waves" viewBox="0 0 560 325" preserveAspectRatio="none" aria-hidden="true">
    <path d="M0,128 C60,185 140,232 260,266 C160,252 60,212 0,172 Z" fill="var(--blue-dark)"/>
    <path d="M0,168 C80,222 200,266 420,298 C470,304 520,300 560,292 L560,325 L0,325 Z" fill="var(--blue-mid)"/>
    <path d="M180,264 C300,292 450,300 560,289 L560,304 C450,312 320,300 180,264 Z" fill="var(--blue-light)"/>
  </svg>
  <div class="card-logo">
    <span class="brand-mark"></span>
    <span class="brand-name">Northgate<br>Claimworks</span>
  </div>
  <div class="card-tagline">Gulf Claims Specialists</div>
  <div class="contact">
    <div class="person">Laura Whitcombe Ellis</div>
    <div class="role">Economic Recovery Consultant</div>
    <div class="address">1830 Harbor Street, Palm Cove, FL 33950</div>
    <div class="row"><span class="label">phone :</span>(555) 017-4820</div>
    <div class="row"><span class="label">email :</span>laura@kducn.com</div>
  </div>
  <div class="site">www.kducn.com</div>
</section>

<section class="card card-back">
  <svg class="waves" viewBox="0 0 560 322" preserveAspectRatio="none" aria-hidden="true">
    <g transform="translate(560,0) scale(-1,1)">
      <path d="M0,135 C60,190 140,236 260,266 C160,254 60,216 0,178 Z" fill="var(--blue-dark)"/>
      <path d="M0,175 C80,226 200,266 420,294 C470,300 520,296 560,288 L560,322 L0,322 Z" fill="var(--blue-mid)"/>
      <path d="M180,264 C300,290 450,296 560,285 L560,300 C450,308 320,298 180,264 Z" fill="var(--blue-light)"/>
    </g>
  </svg>
  <svg class="guide-banner" viewBox="0 0 310 50" preserveAspectRatio="none" aria-hidden="true">
    <polygon points="0,0 310,0 310,34 18,34" fill="var(--blue-dark)"/>
    <rect x="18" y="40" width="292" height="7" fill="var(--blue-light)"/>
  </svg>
  <div class="guide-banner-text">WE WILL BE YOUR GUIDE</div>
  <p class="promise">
    <span class="line-1">You Focus on Your <span class="accent">Business</span>,</span><br>
    <span class="line-2">We’ll Focus on Your <span class="accent">Claim</span></span>
  </p>
  <div class="site">www.kducn.com</div>
</section>

</body>
</html>
```